Business Card Design EFTPOS Comparison site

At QuoteLark.com.au we are a free service that allows our customers to get up to five quotes from our panel of suppliers for a range of BUSINESS related products and services. These products include eftpos / credit card machines, bank accounts, insurance, signage,office furniture etc. basically anything that a small business would need.
The process is done in 3 steps; 1) register your enquiry 2) we source and provide the five cheapest quotes 3) then select the supplier of your choice,the process is simple QuoteLark and is FREE.
Please visit the soon to be revamped website to see our logo.
Target Market(s)
Small business operators
Industry/Entity Type
Small Business
Requirements
Must have
- Double Sided card

```html
<!DOCTYPE html>
<html lang="en">
<head>
<meta charset="utf-8">
<title>QuoteLark Business Card</title>
<link href="https://fonts.googleapis.com/css2?family=Libre+Baskerville:wght@400;700&display=swap" rel="stylesheet">
<style>
  :root {
    --page-bg: #ece8e2;
    --card-bg: #ffffff;
    --orange: #e8871e;
    --orange-dark: #d9761a;
    --blue: #2a6db5;
    --band-text: #fff7ec;
    --band-line: #f6c27a;
    --shadow: rgba(60, 45, 30, 0.22);
  }
  * { box-sizing: border-box; margin: 0; padding: 0; }
  html, body {
    width: 1200px; height: 1200px; overflow: hidden;
    background: var(--page-bg);
    font-family: "Libre Baskerville", Georgia, serif;
  }
  .canvas { position: relative; width: 1200px; height: 1200px; }

  .card {
    position: absolute; left: 190px; width: 820px; height: 470px;
    background: var(--card-bg);
    box-shadow: 4px 6px 14px var(--shadow);
  }
  .card--front { top: 40px; }
  .card--back { top: 620px; }

  .brand {
    position: absolute; display: flex; align-items: center; gap: 14px;
    transform: translate(-50%, -50%);
    color: var(--orange); font-weight: 700; white-space: nowrap;
  }
  .brand__dot { border-radius: 50%; background: var(--blue); flex: none; }
  .card--front .brand { left: 50%; top: 43%; font-size: 72px; }
  .card--front .brand__dot { width: 50px; height: 50px; }
  .card--back .brand { left: 26%; top: 46%; font-size: 46px; gap: 10px; }
  .card--back .brand__dot { width: 32px; height: 32px; }

  .web {
    position: absolute; transform: translateX(-50%);
    color: var(--orange); font-weight: 700; white-space: nowrap;
  }
  .card--front .web { left: 50%; top: 79%; font-size: 20px; }
  .card--back .web { left: 26%; top: 72%; font-size: 18px; }

  .band {
    position: absolute; left: 0; right: 0; top: 90.5%; height: 6%;
    background: linear-gradient(var(--orange) 0%, var(--orange-dark) 100%);
    border-top: 2px solid var(--band-line);
    border-bottom: 2px solid var(--band-line);
    display: flex; align-items: center; justify-content: center;
    color: var(--band-text); font-size: 13px; letter-spacing: 0.6px;
    font-variant: small-caps; white-space: nowrap;
  }

  .divider {
    position: absolute; left: 49%; top: 19%; height: 61%;
    width: 3px; background: var(--orange);
  }

  .contact { position: absolute; left: 62%; top: 19%; }
  .contact__name { font-size: 30px; font-weight: 700; line-height: 1.1; }
  .contact__name .first { color: var(--orange); }
  .contact__name .last { color: var(--blue); }
  .contact__role { color: var(--orange); font-size: 17px; font-weight: 700; margin-top: 6px; }
  .contact__list { list-style: none; margin-top: 54px; font-size: 18px; line-height: 1.6; }
  .contact__list li { white-space: nowrap; }
  .contact__list .gap { margin-top: 14px; }
  .contact__label { color: var(--blue); font-weight: 700; margin-right: 6px; }
  .contact__value { color: var(--orange); font-weight: 700; }
</style>
</head>
<body>
<main class="canvas">
  <section class="card card--front" aria-label="Card front">
    <div class="brand"><span class="brand__dot"></span><span class="brand__name">QuoteLark</span></div>
    <p class="web">www.QuoteLark.com.au</p>
    <div class="band">When we say ‘We guarantee to give you a better EFTPOS deal’ we mean it!</div>
  </section>

  <section class="card card--back" aria-label="Card back">
    <div class="brand"><span class="brand__dot"></span><span class="brand__name">QuoteLark</span></div>
    <p class="web">www.QuoteLark.com.au</p>
    <div class="divider"></div>
    <div class="contact">
      <h1 class="contact__name"><span class="first">Daniel</span> <span class="last">Reyes</span></h1>
      <p class="contact__role">Founder/Owner</p>
      <ul class="contact__list">
        <li><span class="contact__label">P:</span><span class="contact__value">1300.555.214</span></li>
        <li><span class="contact__label">F:</span><span class="contact__value">0000.000.000</span></li>
        <li class="gap"><span class="contact__label">M:</span><span class="contact__value">info@QuoteLark.com</span></li>
        <li><span class="contact__label">W:</span><span class="contact__value">www.QuoteLark.com.au</span></li>
      </ul>
    </div>
    <div class="band">EFTPOS – Credit card machines – Bank accounts – Insurance – Signage – Office furniture</div>
  </section>
</main>
</body>
</html>
```